Zielgruppe
Steuerberatung
Aufgabenstellung
Ich benötige eine Neuerstellung für ein vorhandenes Briefpapier. Bedeutet, eigentlich soll der aktuelle Inhalt neu erstellt werden, da mir die Rohdaten nicht mehr zur Verfügung stehen. Das aktuelle Briefpapier steht als .doc zur Verfügung. Ziel 1:1 Abbildung. Zudem muss die Adresse geändert werden.

```html
<!DOCTYPE html>
<html lang="de">
<head>
<meta charset="utf-8">
<title>Briefpapier Jonas Wellbrock Steuerberater</title>
<link href="https://fonts.googleapis.com/css2?family=Roboto+Condensed:wght@400;700&display=swap" rel="stylesheet">
<style>
  :root {
    --stage: #000000;
    --paper: #ffffff;
    --ink: #111111;
    --accent-grey: #d9dadb;
  }
  * { margin: 0; padding: 0; box-sizing: border-box; }
  html, body {
    width: 1200px; height: 2400px; overflow: hidden;
    background: var(--stage);
  }
  body {
    position: relative;
    font-family: "Roboto Condensed", "Arial Narrow", sans-serif;
    color: var(--ink);
  }
  .sheet {
    position: absolute;
    left: 192px;
    width: 816px;
    height: 1154px;
    background: var(--paper);
    overflow: hidden;
  }
  .sheet--first { top: 35px; }
  .sheet--follow { top: 1210px; }

  .corner-accent {
    position: absolute;
    left: 610px;
    top: 860px;
    width: 300px;
    height: 300px;
    background: var(--accent-grey);
  }

  .sender-line {
    position: absolute;
    left: 77px;
    top: 172px;
    font-size: 9.5px;
    letter-spacing: 0.05px;
    white-space: nowrap;
  }

  .brand {
    position: absolute;
    left: 592px;
    top: 96px;
    display: flex;
    align-items: center;
    gap: 8px;
    font-size: 20px;
    font-weight: 700;
  }
  .brand__square {
    width: 14px; height: 14px;
    background: var(--ink);
  }

  .contact {
    position: absolute;
    left: 592px;
    top: 170px;
    font-size: 12.8px;
    line-height: 16.5px;
    white-space: nowrap;
  }
  .contact__label {
    display: inline-block;
    width: 30px;
  }
  .name { font-weight: 700; }
  .sep { margin: 0 4px; }

  .footer {
    position: absolute;
    left: 77px;
    top: 1066px;
    font-size: 12.3px;
    line-height: 16.8px;
    white-space: nowrap;
  }
</style>
</head>
<body>

<section class="sheet sheet--first">
  <div class="corner-accent"></div>
  <div class="brand"><span class="brand__square"></span><span>Wellbrock</span></div>
  <p class="sender-line">Jonas Wellbrock<span class="sep">|</span>Lindenallee 27<span class="sep">|</span>30159 Lindenstadt</p>
  <div class="contact">
    <p><span class="name">Jonas Wellbrock</span><span class="sep">|</span>Steuerberater</p>
    <p><span class="contact__label">Tel.:</span>+49 (0) 170 - 55 20 631</p>
    <p><span class="contact__label">Fax.:</span>+49 (0) 511 - 22 61 90 48</p>
    <p><span class="contact__label">Mail:</span>info@steuerberatung-wellbrock.de</p>
    <p><span class="contact__label">Web:</span>www.steuerberatung-wellbrock.de</p>
  </div>
  <div class="footer">
    <p><span class="name">Jonas Wellbrock</span><span class="sep">|</span>Steuerberater</p>
    <p>Lindenallee 27<span class="sep">|</span>30159 Lindenstadt<span class="sep">|</span>Zuständige Aufsichtsbehörde: Steuerberaterkammer Nordland -Körperschaft des öffentlichen Rechts-</p>
    <p>Zuständiges Finanzamt: Finanzamt Lindenstadt-Mitte, Steuernummer: 31/208/47116<span class="sep">|</span>Bankverbindung: DE 12 3456 0001 2233 4455 66 BIC: WELBDE2X</p>
  </div>
</section>

<section class="sheet sheet--follow">
  <div class="corner-accent"></div>
  <p class="sender-line">Jonas Wellbrock<span class="sep">|</span>Lindenallee 27<span class="sep">|</span>30159 Lindenstadt</p>
  <div class="footer">
    <p><span class="name">Jonas Wellbrock</span><span class="sep">|</span>Steuerberater</p>
    <p>Lindenallee 27<span class="sep">|</span>30159 Lindenstadt<span class="sep">|</span>Zuständige Aufsichtsbehörde: Steuerberaterkammer Nordland -Körperschaft des öffentlichen Rechts-</p>
    <p>Zuständiges Finanzamt: Finanzamt Lindenstadt-Mitte, Steuernummer: 31/208/47116<span class="sep">|</span>Bankverbindung: DE 12 3456 0001 2233 4455 66 BIC: WELBDE2X</p>
  </div>
</section>

</body>
</html>
```